Brivan Learning Web Design Project

Who We are:
Brivan Learning is education information portal/ magazine, providing information about the Chinese and International education markets. Our aim is to help school principals improve there curriculum, and parents in understanding this curriculum.

Project Brief:
The site will include education news updates, educational services, curriculum developments and overseas study. We hope the site represents the cross cultural bridge between the west and east. The site will cover both the Sciences and Arts.

Note:
The logo design competition is also underway so we only need the website design

What We want:
This competition is for Design only no coding!
Design a home page based on Template 1,2 or 3. I only need to select one.
The design of an article page.

Optional
Design a Microsoft Windows metro style splash page.

Sites We like:
http://www.qz.com.cn/wordsparrow/default.aspx
http://www.velmaracademicpost.co.uk/
http://pvro.orbalinkstudy.net/

Template Explanations:
Template 1-
The main information has a dynamic sliding category view that when clicked displays the relevant info.
In addition to the main upper menu it also has a left hand sliding menu that pops out on click or gesture

Template 2-
Has limited number of Articles most of the menus are drop downs from the top menu

Template 3-
No Top menu

Target Market(s)

Teachers, principals and parents

Industry/Entity Type

Education

Requirements
Should not have
• kindergarten preschool feel

```html
<!DOCTYPE html>
<html lang="en">
<head>
<meta charset="utf-8">
<title>Brivan Learning</title>
<link rel="stylesheet" href="https://fonts.googleapis.com/css2?family=Arimo:wght@400;700&display=swap">
<style>
:root{
  --red:#d9232d;
  --blue:#0f5ea8;
  --blue-dark:#0a4382;
  --text:#111;
  --muted:#8a8a8a;
  --line:#e3e3e3;
  --panel:#f4f4f4;
  --white:#fff;
}
*{box-sizing:border-box;margin:0;padding:0}
html,body{width:1059px;height:1200px;overflow:hidden;background:var(--white);font-family:"Arimo",Arial,sans-serif;color:var(--text)}
.page{position:relative;width:1059px;height:1200px}
.abs{position:absolute}

/* header */
.site-header{left:0;top:0;width:1059px;height:109px;background:linear-gradient(#fdfdfd,#ececec);border-bottom:4px solid var(--red)}
.brand{left:125px;top:62px;display:flex;align-items:center;gap:8px;font-size:17px;font-weight:700;color:var(--red)}
.brand-dot{width:14px;height:14px;border-radius:50%;background:var(--blue)}
.search{left:651px;top:35px;width:284px;height:41px;background:#e4e4e4;border-radius:4px;padding:5px;display:flex}
.search-input{flex:1;background:var(--white);border:1px solid #d6d6d6;border-right:0;font-size:11px;color:#666;padding:9px 10px}
.search-btn{width:74px;background:linear-gradient(#2e7fcc,var(--blue-dark));color:var(--white);font-weight:700;font-size:13px;display:flex;align-items:center;justify-content:center;border-radius:0 2px 2px 0}

/* categories */
.categories{left:126px;top:132px;width:162px;height:457px;background:var(--white);border:1px solid #d8d8d8;box-shadow:0 0 3px rgba(0,0,0,.15);padding:2px}
.categories h2{height:38px;background:linear-gradient(#fff,#e9e9e9);font-size:17px;font-weight:700;padding:10px 10px;border-bottom:1px solid #ddd}
.categories ul{list-style:none;padding:0 4px}
.categories li{height:27.2px;border-bottom:1px dotted #ddd;font-size:11.5px;padding:8px 0 0 26px;position:relative}
.categories li:last-child{border-bottom:0}
.categories li::before{content:"";position:absolute;left:12px;top:11px;border-left:4px solid #aaa;border-top:3px solid transparent;border-bottom:3px solid transparent}

.side-title{font-size:11.5px;font-weight:700;color:var(--red);letter-spacing:.2px}
.follow{left:124px;top:614px}
.social{left:124px;top:637px;width:165px;height:55px;background:var(--panel);display:flex;gap:11px;padding:13px 9px}
.social span{width:28px;height:28px;border-radius:3px}
.s1{background:#5bb6e6}.s2{background:#3b5998}.s3{background:#1b82b7}.s4{background:#d61f20}
.fb-title{left:124px;top:716px;width:165px;padding-bottom:10px;border-bottom:1px solid var(--line)}
.widget{left:124px;top:751px;width:165px;height:239px;border:1px solid #c9c9c9;padding:8px}
.widget-head{display:flex;gap:8px;align-items:flex-start}
.widget-mark{width:34px;height:34px;border-radius:50%;background:var(--blue)}
.widget-name{font-size:11px;font-weight:700;color:#294a8c}
.widget-like{margin-top:4px;width:38px;height:16px;border:1px solid #bcc6da;background:#eef1f7;font-size:9px;color:#3b5998;text-align:center;line-height:14px}
.widget-count{font-size:9px;margin:12px 0 6px}
.widget-count em{font-style:normal;color:#3b5998}
.faces{display:grid;grid-template-columns:repeat(3,41px);gap:3px}
.faces span{height:41px;background:linear-gradient(135deg,#7c8aa0,#c9b59a)}
.widget-foot{margin-top:6px;border-top:1px solid var(--line);padding-top:5px;font-size:8px;color:#555}
.news-title{left:124px;top:1014px;width:165px;padding-bottom:10px;border-bottom:1px solid var(--line)}
.email{left:124px;top:1049px;width:165px;height:25px;border:1px solid #ddd;border-radius:4px;background:#f2f2f2;font-size:11px;color:#555;padding:6px 9px}
.submit{left:124px;top:1085px;width:66px;height:26px;border-radius:4px;background:linear-gradient(#555,#1c1c1c);color:var(--white);font-weight:700;font-size:11.5px;text-align:center;line-height:26px}

/* nav */
.main-nav{left:307px;top:131px;width:628px;height:36px;border-radius:4px;background:linear-gradient(#1d72c0,var(--blue-dark));display:flex}
.main-nav a{color:var(--white);text-decoration:none;font-weight:700;font-size:13px;display:flex;align-items:center;justify-content:center;border-right:1px solid #0a3f78}
.main-nav a:last-child{border-right:0}

/* slider */
.slider{left:307px;top:184px;width:628px;height:285px;background:linear-gradient(100deg,#e4e4e2 0%,#cfc8c0 40%,#9db0c8 60%,#d8cfc6 100%)}
.dots{left:583px;top:460px;width:78px;height:17px;background:var(--white);border-radius:8px 8px 0 0;display:flex;gap:5px;justify-content:center;align-items:center}
.dots span{width:8px;height:8px;border-radius:50%;background:#c8c8c8}
.dots span:first-child{background:var(--red)}

/* tabs & articles */
.tab{top:486px;height:41px;font-size:14px;font-weight:700;text-align:center;line-height:41px;border-radius:3px 3px 0 0}
.tab-sciences{left:318px;width:115px;background:var(--white);color:var(--red);border:1px solid var(--line);border-bottom:0;border-top:3px solid var(--line);z-index:2}
.tab-arts{left:437px;width:115px;background:#dedede;color:#9a9a9a;top:487px}
.feed{left:307px;top:526px;width:446px;height:608px;border:1px solid var(--line);border-radius:0 0 3px 3px;padding:10px 11px}
.post{display:flex;gap:13px;height:154px;border-bottom:1px solid var(--line);padding-top:1px}
.post:last-child{border-bottom:0}
.thumb{width:104px;height:104px;background:#e6e6e6;padding:5px;flex:none}
.thumb div{width:100%;height:100%}
.t1{background:linear-gradient(135deg,#4a6a94,#cfd9e6)}
.t2{background:radial-gradient(circle,#e2a24a,#1a1a1a 70%)}
.t3{background:linear-gradient(135deg,#f3efe6,#b9b1a2)}
.t4{background:linear-gradient(135deg,#2c2c2c,#9fa7a4)}
.post-body{width:305px}
.post h3{font-size:13px;line-height:17px;font-weight:700;margin-top:-1px}
.post p{font-size:10.5px;line-height:16.4px;color:var(--muted);margin-top:5px}
.post a{display:block;margin-top:6px;font-size:9.5px;color:var(--blue);text-decoration:none}

/* right column */
.updates-title{left:769px;top:483px}
.updates{left:769px;top:505px;width:166px}
.update{border-top:1px solid var(--line);height:119px;padding-top:11px}
.update h4{font-size:10.5px;font-weight:400;line-height:15px}
.update p{font-size:9.5px;line-height:13.5px;color:var(--muted);margin-top:4px}
.more{display:flex;justify-content:flex-end;align-items:center;gap:5px;font-size:9px;margin-top:5px}
.more svg{width:15px;height:15px}
.articles-title{left:769px;top:860px;width:166px;border-top:2px solid #ccc;padding-top:13px}
.article-list{left:769px;top:895px;width:166px;list-style:none}
.article-list li{font-size:10.5px;line-height:15px;padding:8px 0 7px 12px;border-bottom:1px solid var(--line);position:relative}
.article-list li:last-child{border-bottom:0}
.article-list li::before{content:"";position:absolute;left:2px;top:14px;border-left:3px solid #999;border-top:3px solid transparent;border-bottom:3px solid transparent}

/* footer */
.site-footer{left:124px;top:1158px;width:811px;border-top:2px solid var(--red);display:flex;justify-content:space-between;padding-top:15px;font-size:10.5px;color:#444}
.footer-nav{display:flex;gap:36px}
</style>
</head>
<body>
<div class="page">
  <header class="abs site-header"></header>
  <div class="abs brand"><span class="brand-dot"></span>Brivan Learning</div>
  <div class="abs search"><div class="search-input">Search</div><div class="search-btn">SEARCH</div></div>

  <aside class="abs categories">
    <h2>Categories</h2>
    <ul>
      <li>Lorem ipsum dolor</li><li>Lorem ipsum dolor</li><li>Lorem ipsum dolor</li><li>Lorem ipsum dolor</li><li>Lorem ipsum dolor</li>
      <li>Lorem ipsum dolor</li><li>Lorem ipsum dolor</li><li>Lorem ipsum dolor</li><li>Lorem ipsum dolor</li><li>Lorem ipsum dolor</li>
      <li>Lorem ipsum dolor</li><li>Lorem ipsum dolor</li><li>Lorem ipsum dolor</li><li>Lorem ipsum dolor</li><li>Lorem ipsum dolor</li>
    </ul>
  </aside>

  <div class="abs side-title follow">FOLLOW US</div>
  <div class="abs social"><span class="s1"></span><span class="s2"></span><span class="s3"></span><span class="s4"></span></div>

  <div class="abs side-title fb-title">CIRCLEBOOK</div>
  <div class="abs widget">
    <div class="widget-head">
      <div class="widget-mark"></div>
      <div><div class="widget-name">Brivan Learning</div><div class="widget-like">Like</div></div>
    </div>
    <div class="widget-count">13,223 people like <em>Brivan Learning</em>.</div>
    <div class="faces" role="img" aria-label="Grid of follower profile photos">
      <span></span><span></span><span></span><span></span><span></span><span></span><span></span><span></span><span></span>
    </div>
    <div class="widget-foot">Circlebook social plugin</div>
  </div>

  <div class="abs side-title news-title">SIGN UP FOR NEWSLETTER</div>
  <div class="abs email">E-mail</div>
  <div class="abs submit">SUBMIT</div>

  <nav class="abs main-nav">
    <a href="#" style="width:85px">HOME</a>
    <a href="#" style="width:111px">ABOUT US</a>
    <a href="#" style="width:125px">CATEGORIES</a>
    <a href="#" style="width:104px">ARTICLES</a>
    <a href="#" style="width:80px">BLOG</a>
    <a href="#" style="width:123px">CONTACT US</a>
  </nav>

  <div class="abs slider" role="img" aria-label="Smiling teacher and students in a science classroom in front of a periodic table"></div>
  <div class="abs dots"><span></span><span></span><span></span><span></span><span></span></div>

  <div class="abs tab tab-sciences">SCIENCES</div>
  <div class="abs tab tab-arts">ARTS</div>
  <section class="abs feed">
    <article class="post">
      <div class="thumb"><div class="t1" role="img" aria-label="Student in safety goggles doing a lab experiment"></div></div>
      <div class="post-body">
        <h3>Lorem ipsum dolor sit amet, consectetur adipisicing elit, sed do eiusmod tempor incididunt</h3>
        <p>Sed ut perspiciatis unde omnis iste natus error sit voluptatem accusantium doloremque laudantium, totam rem aperiam, eaque ipsa quae ab illo inventore veritatis et quasi architecto beatae vitae dicta sunt explicabo.</p>
        <a href="#">Full Article ›</a>
      </div>
    </article>
    <article class="post">
      <div class="thumb"><div class="t2" role="img" aria-label="Colourful icons rising from an open book"></div></div>
      <div class="post-body">
        <h3>Lorem ipsum dolor sit amet, consectetur adipisicing elit, sed do eiusmod tempor incididunt</h3>
        <p>Sed ut perspiciatis unde omnis iste natus error sit voluptatem accusantium doloremque laudantium, totam rem aperiam, eaque ipsa quae ab illo inventore veritatis et quasi architecto beatae vitae dicta sunt explicabo.</p>
        <a href="#">Full Article ›</a>
      </div>
    </article>
    <article class="post">
      <div class="thumb"><div class="t3" role="img" aria-label="Fountain pen on a dictionary entry for education"></div></div>
      <div class="post-body">
        <h3>Lorem ipsum dolor sit amet, consectetur adipisicing elit, sed do eiusmod tempor incididunt</h3>
        <p>Sed ut perspiciatis unde omnis iste natus error sit voluptatem accusantium doloremque laudantium, totam rem aperiam, eaque ipsa quae ab illo inventore veritatis et quasi architecto beatae vitae dicta sunt explicabo.</p>
        <a href="#">Full Article ›</a>
      </div>
    </article>
    <article class="post">
      <div class="thumb"><div class="t4" role="img" aria-label="Stack of books beside an e-reader"></div></div>
      <div class="post-body">
        <h3>Lorem ipsum dolor sit amet, consectetur adipisicing elit, sed do eiusmod tempor incididunt</h3>
        <p>Sed ut perspiciatis unde omnis iste natus error sit voluptatem accusantium doloremque laudantium, totam rem aperiam, eaque ipsa quae ab illo inventore veritatis et quasi architecto beatae vitae dicta sunt explicabo.</p>
        <a href="#">Full Article ›</a>
      </div>
    </article>
  </section>

  <div class="abs side-title updates-title">EDUCATION NEWS UPDATES</div>
  <div class="abs updates">
    <div class="update">
      <h4>Lorem ipsum dolor sit amet, consectetur adipisicing elit</h4>
      <p>Sed ut perspiciatis unde omnis iste natus error sit voluptatem accu santium doloremque</p>
      <div class="more">Learn more <svg viewBox="0 0 16 16"><circle cx="8" cy="8" r="7" fill="none" stroke="#333" stroke-width="1.4"/><path d="M5 8h6M8.5 5.5 11 8l-2.5 2.5" fill="none" stroke="#333" stroke-width="1.4"/></svg></div>
    </div>
    <div class="update">
      <h4>Lorem ipsum dolor sit amet, consectetur adipisicing elit</h4>
      <p>Sed ut perspiciatis unde omnis iste natus error sit voluptatem accu santium doloremque</p>
      <div class="more">Learn more <svg viewBox="0 0 16 16"><circle cx="8" cy="8" r="7" fill="none" stroke="#333" stroke-width="1.4"/><path d="M5 8h6M8.5 5.5 11 8l-2.5 2.5" fill="none" stroke="#333" stroke-width="1.4"/></svg></div>
    </div>
    <div class="update">
      <h4>Lorem ipsum dolor sit amet, consectetur adipisicing elit</h4>
      <p>Sed ut perspiciatis unde omnis iste natus error sit voluptatem accu santium doloremque</p>
      <div class="more">Learn more <svg viewBox="0 0 16 16"><circle cx="8" cy="8" r="7" fill="none" stroke="#333" stroke-width="1.4"/><path d="M5 8h6M8.5 5.5 11 8l-2.5 2.5" fill="none" stroke="#333" stroke-width="1.4"/></svg></div>
    </div>
  </div>

  <div class="abs side-title articles-title">ARTICLES</div>
  <ul class="abs article-list">
    <li>Quisque lacinia ligula ac lobortis luctus.</li>
    <li>Vestibulum lobortis leo ac odio rutrum auctor.</li>
    <li>Nunc eget mauris eget quam aliquet commodo in et velit.</li>
    <li>Aenean porttitor ipsum sed lacus semper, ut sodales neque consequat.</li>
    <li>Maecenas sed tellus bibendum, cursus dui et, consequat sapien.</li>
  </ul>

  <footer class="abs site-footer">
    <span>Copyright © 2013 Brivan Learning. All rights reserved.</span>
    <span class="footer-nav"><span>Home</span><span>About Us</span><span>Categories</span><span>Articles</span><span>BLog</span><span>Contact Us</span></span>
  </footer>
</div>
</body>
</html>
```